Personal Development Book for Millennials Needs a Cover Design

Book Title: Salt Horizon: A Dreamer's Map to Being, 15 "No Escape" Queries on Joy, Routines and Grit for Muddled Millennials
Author's Name: Marcus T. Oldenfrey
Salt Horizon: A Dreamer's Map to Being is a collection of raw, unfiltered and personal essays on happiness, habits and hustle. It is a compilation of 15 provocative, yet fundamental questions that every mixed-up millennial or twenty-something should answer in order to live a life full of energy and excitement rather than monotony and mediocrity.
It is a personal development book written by a regular, twenty-something dude who got tired of doing boring things. He then quit his job, fell off a motorcycle somewhere near the equator, and came back to the States and immediately started writing.
"Pura vida," the law of the land in Costa Rica, translates to "pure life." "Pura vida" is more than just a greeting; it is an embodiment of the Costa Rican people, who find immense happiness in life's little pleasures, preferring to lay low, live slow and live purposefully. "Pura vida" is another way of saying "relax and take it easy."
The goal of the book is to stand out on the Zelvora platform as a small thumbnail. The imagery should make the viewer feel that the book (and the author) is an authority on the topic of self-discovery, self-awareness, and purposeful, intentional living.
The reader should feel that they MUST read this book if they are the least bit confused, anxious, mixed-up or desperately trying to figure out how to take back control of their own life and start doing the things that excite them. It's more important that the book "pops off the shelf" or stands out and catches the eye quickly.
The most important part of the design is that it is clean, uncluttered and simple. It should embody the "pura vida" lifestyle. I am open to any image or illustration you choose.
I like a bold color palette, and I'd like to see green be the primary color used in the design. Lush, greenery is everywhere in Costa Rica. Green also represents life, very appropriate for this book. I like bold titles that are easy to recognize and comprehend. Please use no more than 2-3 colors.
Zelvora eBook covers I particularly like:
Print Liftoff by Wesley Harrow
A Man Near The Pier by Neil Dorsey
Inner Steel — 48 Tested Paths to Build Inner Steel, Lift Your Morale and Quiet Inner Worry by Rory M.T. Pask
Hour Mastery: Peak Output by Owen Farrukh
Target Market(s)
Millennials
Requirements
Must have
- This book is intended to encourage millennials to do some soul-searching, think and WRITE down their own answers to the questions in this book. It is a book that should be read with a notebook and a pen close by.
- I'd like to see covers that subtly hint at this fact. Please reference the example covers listed in the project description to best match the style of cover I am looking for. If it is clear that you have NOT referenced the example covers, your design will be eliminated.
Nice to have
- If possible, would like to see designs that include the following three components WITHOUT making the cover feel too busy or cluttered:
- 1) Pen
- 2) Paper
- 3) Beach
Should not have
- Cover should NOT look or feel as if this is a book about environmentalism. Trees, plants, greenery, etc. should NOT be the primary focal point of the cover design. If included, these elements should be additive.

```html
<!DOCTYPE html>
<html lang="en">
<head>
<meta charset="utf-8">
<title>Salt Horizon: A Dreamer's Map to Being</title>
<link rel="stylesheet" href="https://fonts.googleapis.com/css2?family=Montserrat:wght@400;500;700&display=swap">
<style>
  :root {
    --paper: #ffffff;
    --paper-shade: #d9d9d9;
    --green-deep: #74bb3c;
    --green-mid: #9fd45f;
    --green-light: #d4edaa;
    --ink-light: #ffffff;
    --ink-soft: #f4fbe8;
    --accent: #f7941d;
  }
  * { margin: 0; padding: 0; box-sizing: border-box; }
  html, body { width: 800px; height: 1200px; overflow: hidden; background: var(--paper); }
  .cover {
    position: relative;
    width: 800px;
    height: 1200px;
    overflow: hidden;
    font-family: "Montserrat", Arial, sans-serif;
    background: radial-gradient(circle at 400px 420px, var(--green-light) 0, var(--green-mid) 380px, var(--green-deep) 760px);
  }
  .halo {
    position: absolute;
    left: 170px; top: 175px;
    width: 460px; height: 460px;
    border-radius: 50%;
    background: radial-gradient(circle, rgba(255,255,255,0.28) 0, rgba(255,255,255,0.12) 70%, rgba(255,255,255,0.18) 100%);
    border: 2px solid rgba(255,255,255,0.25);
  }
  .torn-edge { position: absolute; left: 0; width: 800px; }
  .torn-edge--top { top: 0; height: 140px; }
  .torn-edge--bottom { bottom: 0; height: 120px; }
  .title {
    position: absolute;
    top: 150px; left: 0; width: 800px;
    text-align: center;
    color: var(--ink-light);
    font-weight: 700;
    font-size: 66px;
    letter-spacing: 1px;
  }
  .tagline {
    position: absolute;
    top: 340px; left: 0; width: 800px;
    text-align: center;
    color: var(--ink-soft);
    font-weight: 400;
    font-size: 48px;
    line-height: 60px;
    letter-spacing: 1px;
  }
  .subtitle {
    position: absolute;
    top: 638px; left: 0; width: 800px;
    display: flex;
    justify-content: center;
    align-items: center;
    gap: 12px;
    color: var(--ink-light);
  }
  .subtitle__count { font-weight: 700; font-size: 92px; line-height: 1; }
  .subtitle__text { font-weight: 500; font-size: 25px; line-height: 36px; }
  .subtitle__key { color: var(--accent); }
  .author {
    position: absolute;
    top: 985px; left: 0; width: 800px;
    text-align: center;
    color: var(--ink-light);
    font-weight: 500;
    font-size: 28px;
    letter-spacing: 3px;
  }
</style>
</head>
<body>
<main class="cover">
  <div class="halo"></div>

  <svg class="torn-edge torn-edge--top" viewBox="0 0 800 140" preserveAspectRatio="none">
    <polygon fill="var(--paper-shade)" points="0,0 800,0 800,40 770,46 740,38 700,52 660,44 620,60 590,50 560,66 520,58 480,72 450,62 410,78 370,70 330,84 300,76 260,92 220,84 190,98 150,90 110,104 80,96 40,110 0,102"/>
    <polygon fill="var(--paper)" points="0,0 800,0 800,34 770,40 740,32 700,46 660,38 620,54 590,44 560,60 520,52 480,66 450,56 410,72 370,64 330,78 300,70 260,86 220,78 190,92 150,84 110,98 80,90 40,104 0,96"/>
  </svg>

  <h1 class="title">SALT HORIZON</h1>
  <p class="tagline">A DREAMER'S<br>MAP TO BEING</p>

  <div class="subtitle">
    <span class="subtitle__count">15</span>
    <p class="subtitle__text">"No Escape" Queries on <span class="subtitle__key">Joy</span>,<br><span class="subtitle__key">Routines</span> and <span class="subtitle__key">Grit</span> for Muddled Millennials</p>
  </div>

  <p class="author">MARCUS T. OLDENFREY</p>

  <svg class="torn-edge torn-edge--bottom" viewBox="0 0 800 120" preserveAspectRatio="none">
    <polygon fill="var(--paper-shade)" points="0,28 40,34 80,22 120,36 160,26 200,40 240,30 280,44 320,34 360,48 400,38 440,52 480,42 520,56 560,46 600,60 640,50 680,64 720,54 760,68 800,58 800,120 0,120"/>
    <polygon fill="var(--paper)" points="0,34 40,40 80,28 120,42 160,32 200,46 240,36 280,50 320,40 360,54 400,44 440,58 480,48 520,62 560,52 600,66 640,56 680,70 720,60 760,74 800,64 800,120 0,120"/>
  </svg>
</main>
</body>
</html>
```